Card for Maori themed strategy game

Visual design of a type of card from a board game.
The card has a front and a back, back being a single large image, and with one of three small icons (in white) to represent which of the three periods of the game it is from, but otherwise there is no difference in the backs.
The front side carries most of the information, and hopefully an attractive design. Functionally, from top to bottom it has a title, a large text field, a type line, another text field, and some tracking information at the very bottom. Current layout with placeholder art is attached.
Note that the relative size of the two text boxes will vary from card to card.
The colour pallete is intended to be red black and white, for this particular design focusing primarily on red.

```html
<!DOCTYPE html>
<html lang="en">
<head>
<meta charset="utf-8">
<title>Claiming the land – card back and front</title>
<link href="https://fonts.googleapis.com/css2?family=Montserrat:wght@700&family=PT+Sans&display=swap" rel="stylesheet">
<style>
  :root {
    --page-bg: #f2f2f2;
    --card-red-light: #c5262d;
    --card-red-dark: #5f0b0c;
    --art-red: #e3242a;
    --art-deep: #7a0d10;
    --ink: #120203;
    --panel: rgba(128, 16, 18, 0.88);
    --white: #ffffff;
  }
  * { box-sizing: border-box; margin: 0; padding: 0; }
  html, body {
    width: 1200px; height: 1200px; overflow: hidden;
    background: var(--page-bg);
  }
  .canvas { position: relative; width: 1200px; height: 1200px; }

  .card {
    position: absolute; top: 323px;
    width: 395px; height: 553px;
    background: linear-gradient(90deg, var(--card-red-light), var(--card-red-dark));
    border: 1px solid #3a0506;
  }
  .card--back { left: 111px; }
  .card--front { left: 693px; }

  .card__frame {
    position: absolute; left: 22px; top: 29px;
    width: 350px; height: 494px;
    border: 4px solid var(--ink);
    border-radius: 12px;
    overflow: hidden;
  }
  .card__art {
    position: absolute; inset: 0;
    background:
      radial-gradient(ellipse at 50% 45%, var(--art-red) 0%, #c81b20 45%, var(--art-deep) 80%, var(--ink) 100%);
  }
  .card--front .card__art {
    background:
      radial-gradient(ellipse at 50% 50%, #8e1417 0%, #5a0a0c 55%, var(--ink) 100%);
  }

  .period-notch {
    position: absolute; left: 0; bottom: 0; width: 100%; height: 60px;
  }

  .card__title,
  .card__type {
    position: absolute; left: 0; width: 100%;
    font-family: "Montserrat", sans-serif; font-weight: 700;
    color: var(--white); text-align: center; line-height: 1;
  }
  .card__title { top: 6px; font-size: 31px; letter-spacing: 0.2px; }
  .card__type { top: 163px; font-size: 38px; }

  .text-box {
    position: absolute; left: 22px; width: 302px;
    background: var(--panel);
    display: flex; align-items: center; justify-content: center;
    font-family: "PT Sans", sans-serif; font-size: 26px;
    line-height: 34px; color: var(--white); text-align: center;
  }
  .text-box--effect { top: 44px; height: 107px; }
  .text-box--reaction { top: 209px; height: 234px; padding-bottom: 8px; }
</style>
</head>
<body>
<main class="canvas">

  <section class="card card--back" aria-label="Card back">
    <div class="card__frame">
      <div class="card__art" role="img" aria-label="Carved Maori-style mask artwork in red and black with yellow eyes"></div>
      <svg class="period-notch" viewBox="0 0 342 60" aria-hidden="true">
        <defs>
          <linearGradient id="notchFill" x1="0" x2="1">
            <stop offset="0" stop-color="#a81b21"/>
            <stop offset="1" stop-color="#7c1013"/>
          </linearGradient>
        </defs>
        <path d="M118 60 V50 A53 53 0 0 1 224 50 V60 Z" fill="url(#notchFill)" stroke="#3a0506" stroke-width="2"/>
        <circle cx="171" cy="40" r="11" fill="#ffffff"/>
      </svg>
    </div>
  </section>

  <section class="card card--front" aria-label="Card front">
    <div class="card__frame">
      <div class="card__art" role="img" aria-label="Faded red and black Maori-style pattern behind the card text"></div>
      <h2 class="card__title">Claiming the land</h2>
      <p class="text-box text-box--effect">Sed ut perspiciatis unde<br>omnis iste natus error</p>
      <h3 class="card__type">Reaction</h3>
      <p class="text-box text-box--reaction">Excepteur sint occaecat<br>cupidatat non proident,<br>sunt in culpa qui officia<br>deserunt mollit anim id<br>est laborum</p>
    </div>
  </section>

</main>
</body>
</html>
```